Tri-Fold Flyer for Powder Coating Company

We need a new professional tri-fold flyer designed for our powder coating company. These will be used at trade shows and while on sales calls so they should cover all our services. I have attached two old tri-folds we used in the past for reference. We are looking for a clean and fresh professional design and you should use our website (www.finishcoatingworks.com) as a reference for services we provide. I have also attached our logo and a business card we just had designed on ArtworkHive. We are giong to be centering our future design and branding around this business card design. If further stock is necessary, please let me know. Note: We no longer do chrome plating.

Contact info that should be supplied on flyer:

Phone: 309.547.2618
Email: info@finishcoatingworks.com
Web: www.finishcoatingworks.com
Facebook: www.facebook.com/finishcoatingworks

Our website should be very prominently promoted throughout this flyer as well as our Facebook page.

Target Market(s)

We are promoting ourselves to industrial equipment manufactures (Like Brandolex, Vorenta & Pete Halvor) as well as private individuals that are restoring old cars and restoring lawn furniture.

Industry/Entity Type

It Company

Font styles to use
Sans Serif

Requirements
Must have
• It should be similar in style to our website and business card design.

```html
<!DOCTYPE html>
<html lang="en">
<head>
<meta charset="utf-8">
<title>Finish Coating Works – Tri-Fold Inside Spread</title>
<link href="https://fonts.googleapis.com/css2?family=Open+Sans:ital,wght@0,400;0,600;0,700;0,800;1,400;1,600;1,700&display=swap" rel="stylesheet">
<style>
  :root {
    --red: #e11d26;
    --red-dark: #b5121a;
    --yellow: #f2e21a;
    --ink: #3a3a3a;
    --grey-bg: #d9d9d9;
    --paper: #ffffff;
    --paper-tint: #f1f1f1;
    --photo-grey: #8f9498;
    --photo-green: #b7c94a;
  }
  * { box-sizing: border-box; margin: 0; padding: 0; }
  html, body { width: 1200px; height: 960px; overflow: hidden; }
  body {
    background: var(--grey-bg);
    font-family: "Open Sans", sans-serif;
    color: var(--ink);
  }
  .spread {
    position: absolute; left: 36px; top: 44px;
    width: 1128px; height: 872px;
    background: linear-gradient(180deg, var(--paper) 0%, var(--paper-tint) 100%);
    overflow: hidden;
    box-shadow: 0 6px 24px rgba(0,0,0,.18);
  }
  .panel {
    position: absolute; top: 0; width: 376px; height: 872px;
    overflow: hidden;
  }
  .panel--services { left: 0; }
  .panel--ceramic { left: 376px; }
  .panel--stripping { left: 752px; }
  .panel-text {
    position: relative; z-index: 2;
    padding: 0 26px;
    font-size: 9.6px; line-height: 13px;
  }
  p { margin-bottom: 6px; text-align: justify; }
  .section-title {
    color: var(--red); font-weight: 800; font-size: 13px;
    text-transform: uppercase; letter-spacing: .2px; margin: 6px 0 3px;
  }
  .question { font-size: 12.5px; font-weight: 400; margin: 6px 0 3px; }
  .question--italic { font-style: italic; text-align: center; }
  .callout { font-style: italic; font-weight: 700; font-size: 11.5px; line-height: 14px; margin: 8px 0; }
  .callout--big { font-style: normal; font-size: 13px; line-height: 16px; }

  .pill {
    display: block; width: 170px; margin: 30px auto 8px;
    background: var(--red); color: #fff; text-align: center;
    border-radius: 14px; font-size: 12px; letter-spacing: 2px; padding: 4px 0;
  }
  .item-list { display: flex; gap: 20px; margin: 2px 0 4px; font-size: 9.6px; line-height: 12.6px; }
  .item-list ul { list-style: none; flex: 1; }
  .item-list-more { text-align: right; font-size: 9.6px; margin-bottom: 6px; }

  .car-photo {
    position: absolute; left: 0; bottom: 120px; width: 376px; height: 260px; z-index: 1;
    background: linear-gradient(180deg, rgba(255,255,255,0) 0%, rgba(150,160,150,.35) 60%, rgba(120,150,90,.45) 100%);
  }
  .top-swoosh { position: absolute; top: 0; left: 0; z-index: 1; }
  .lantern-photo {
    position: absolute; left: 30px; top: 12px; width: 120px; height: 120px; z-index: 3;
    border-radius: 50%; border: 5px solid #fff;
    background: radial-gradient(circle at 50% 45%, #c8242a 0%, #7a2a2a 45%, #4d5a50 100%);
    box-shadow: 0 2px 6px rgba(0,0,0,.3);
  }
  .panel--ceramic .panel-text { padding-top: 150px; }

  .spray-photo {
    position: absolute; left: 0; top: 0; width: 376px; height: 190px; z-index: 1;
    background: linear-gradient(120deg, var(--photo-grey) 0%, #a9ad9c 40%, var(--photo-green) 60%, #c5c8c8 80%, #d5d6d6 100%);
  }
  .top-wave { position: absolute; left: 0; top: 140px; z-index: 2; }
  .panel--stripping .panel-text { padding-top: 190px; }

  .bottom-band { position: absolute; left: 0; bottom: 0; z-index: 4; }
  .web-address {
    position: absolute; left: 26px; bottom: 36px; z-index: 5;
    color: #fff; font-size: 17px; letter-spacing: .3px;
  }
  .brand {
    position: absolute; right: 28px; bottom: 38px; z-index: 5;
    display: flex; align-items: center; gap: 8px;
    color: var(--yellow); font-weight: 800; font-size: 21px; text-transform: uppercase;
  }
  .brand-dot { width: 14px; height: 14px; border-radius: 50%; background: var(--yellow); }
</style>
</head>
<body>
<main class="spread">

  <section class="panel panel--services">
    <div class="car-photo" role="img" aria-label="Faded photo of a restored classic car on grass"></div>
    <div class="panel-text">
      <span class="pill">SERVICES</span>
      <h2 class="section-title">Custom Powder Coating</h2>
      <p>Finish Coating Works can custom coat virtually any new or used metal object you may have around your home that needs restored, refreshed or coated.</p>
      <h3 class="question">What is powder coating?</h3>
      <p>Powder coating is a type of coating that is applied as a free-flowing, dry powder. The main difference between a conventional liquid paint and powder coating is that the powder coating does not require a solvent to keep the binder and filler parts in a liquid suspension form. Our custom powder coating is typically applied electrostatically and is then cured in an oven to allow it to flow and form a “skin”. The coating creates a hard finish that is tougher and longer lasting than conventional paint.</p>
      <h3 class="question">What can be powder coated?</h3>
      <div class="item-list">
        <ul>
          <li>Automotive Frames &amp; Parts</li>
          <li>Classic Car Chassis &amp; Parts</li>
          <li>Race Car Chassis &amp; Components</li>
          <li>Truck Bumpers &amp; Grill Guards</li>
          <li>Motorcycle Frames &amp; Parts</li>
          <li>Wheels</li>
          <li>Indoor &amp; Outdoor Furniture</li>
          <li>Metal Gliders &amp; Chairs</li>
          <li>Antique Gas Pumps</li>
          <li>Outdoor Yard Ornaments</li>
        </ul>
        <ul>
          <li>Exercise Equipment</li>
          <li>Lighting Fixtures</li>
          <li>Cabinet Hardware</li>
          <li>Bicycle Frames &amp; Parts</li>
          <li>ATV Frames &amp; Accessories</li>
          <li>Metal Fences &amp; Railings</li>
          <li>Industrial Parts</li>
          <li>Food Handling Equipment</li>
          <li>Retail &amp; Office Displays</li>
          <li>Outdoor Signage</li>
        </ul>
      </div>
      <p class="item-list-more">… among many, many more things!</p>
      <p class="callout callout--big">Save money by restoring your items<br>For a fraction of the price of buying new!</p>
      <h2 class="section-title">Commercial Coating Services</h2>
      <p>At Finish Coating Works, we have spent many years positioning ourselves to become a partner for your commercial, industrial or manufacturing projects. We understand that in today’s world of quick turnaround times and tight profit margins you need a reliable business partner and we are here to provide just that with efficient turnaround times and competitive pricing. Our commercial coating services can make the difference between delivering on time and missing your window of opportunity to impress your customer. We don’t differentiate between a prototype product or a large production run – we will make your project a priority!</p>
    </div>
  </section>

  <section class="panel panel--ceramic">
    <svg class="top-swoosh" width="376" height="110" viewBox="0 0 376 110" aria-hidden="true">
      <path d="M0,0 H376 V8 C260,30 150,50 0,105 Z" fill="#bfc1c3"/>
      <path d="M0,0 H376 V4 C260,24 150,42 0,95 Z" fill="#d6d7d8"/>
    </svg>
    <div class="lantern-photo" role="img" aria-label="Close-up photo of a red powder-coated lantern"></div>
    <div class="panel-text">
      <p>Even though powder coating offers a superior finish that can extend the life of your part, not all powder coated finishes are created equal. Preparation before the powder coating process is the key to our proven success. We achieve outstanding powder coat durability for all our customers by using the latest technology for surface preparation available to ensure the best powder adhesion and long term performance of the final product. We have a very specific process and quality control standards for every part to ensure the proper powder adhesion.</p>
      <p class="callout">Our proficient staff has dozens of years of experience in powder coating</p>
      <h2 class="section-title">High Temperature Ceramic Coating</h2>
      <p>Finish Coating Works is proud to offer high temperature ceramic coatings capable of withstanding the harshest under-hood conditions. Whether you are trying to win a trophy in the next show or achieve that next level of performance on the track, we can fulfill your high-temperature coating needs.</p>
      <p>High temperature ceramic coating offers many performance enhancing benefits while helping to protect your parts. These coatings have a very good chemical and corrosion resistance and possess excellent thermal barrier characteristics, providing a dramatic reduction in radiated heat.</p>
      <p>This means reduced under-hood temperatures, accelerated exhaust gas velocity and a longer life expectancy for the entire exhaust system. When cured, a very effective corrosion inhibiting film is formed that protects the part against oxidation and imparts excellent chemical resistance that further extends part life and enhances appearance.</p>
      <h3 class="question question--italic">Uses for High-Temperature Ceramic Coating?</h3>
      <p><em>Many people already know that high-temperature ceramic coats are used to coat original equipment exhaust manifolds and aftermarket headers, but they may not know some of the other applications for the same products. A few of those applications are boat parts, motorcycle parts, tractor parts and snowmobile parts … among so many more.</em></p>
    </div>
  </section>

  <section class="panel panel--stripping">
    <div class="spray-photo" role="img" aria-label="Photo of a worker in a protective suit spraying green powder coat onto a metal panel"></div>
    <svg class="top-wave" width="376" height="60" viewBox="0 0 376 60" aria-hidden="true">
      <path d="M0,0 C120,40 260,40 376,20 V60 H0 Z" fill="var(--red)"/>
      <path d="M0,14 C120,52 260,52 376,34 V60 H0 Z" fill="#ffffff"/>
    </svg>
    <div class="panel-text">
      <h2 class="section-title">Metal Parts Stripping and Cleaning</h2>
      <p>With our proven pyrolytic thermal extraction metal cleaning method we will easily clean multiple layers of paint and powder coating from steel substrate. From removing paint from automobile parts such as hoods and fenders to cleaning virtually any steel parts for manufacturing facilities, we can strip virtually any steel parts with ease and achieve outstanding results.</p>
      <p>What about parts that aren’t steel? We can also chemically strip paint from aluminum components. This will leave your parts completely bare and ready for whatever you choose to do with them.</p>
      <p>Our metal cleaning capabilities don’t stop at paint and powder coating. In the past we have cleaned components for food manufacturing factories and industrial equipment manufacturing facilities.</p>
      <h2 class="section-title">Fuel Tank Revive</h2>
      <p>TankRevive is a patented, chemical bonding repair process which coats the inside and outside of your fuel tank. This double layer of protection completely seals the tank, preventing rust and corrosion… forever! This process is ideal for hard to find classic car tanks and extremely expensive large tanks.</p>
      <h3 class="question">What type of tanks can be coated?</h3>
      <p>Revive Coating can be used on virtually any type of tank, but it is ideal for use on classic car tanks (that are no longer available as new) or large truck or industrial tanks (that are quite expensive to replace). If your tank is irreplaceable or custom built, Revive coating is perfect for you. We can save tanks that many people think are too far gone. In fact, we have repaired and coated tanks that have literally thousands of holes in them. On the other hand, you may have a tank that costs over $1000 to replace that can be repaired and coated for a fraction of the price. In fact, after our coating your tank will be better than new!</p>
    </div>
  </section>

  <svg class="bottom-band" width="1128" height="150" viewBox="0 0 1128 150" aria-hidden="true">
    <path d="M0,30 C300,62 760,64 1128,22 V150 H0 Z" fill="#d8d8d8"/>
    <path d="M0,40 C300,72 760,74 1128,32 V150 H0 Z" fill="var(--yellow)"/>
    <path d="M0,52 C300,84 760,86 1128,44 V150 H0 Z" fill="var(--red)"/>
    <path d="M0,110 C300,128 760,130 1128,100 V150 H0 Z" fill="var(--red-dark)" opacity=".35"/>
  </svg>
  <div class="web-address">www.finishcoatingworks.com</div>
  <div class="brand"><span class="brand-dot"></span>Finish Coating Works</div>

</main>
</body>
</html>
```